Brindlewave Systems Retractable Banner

Need a design for a retractable banner (approx. 63 inches x 24 inches) Provide us with different raw file types including: ai, png. We may end up ordering a banner that is larger or smaller so please ensure the design provided can be scaled accordingly.
Key Features:
One of the two logos shown below must be displayed (your choice). We can provide other file formats for the logo if needed.
Words that have to be shown:
Your *Data Collection Problems* End Here
Our technology transforms any building into an *IoT Smart Building*
Our *Monitoring and Alerting* capabilities give you full insight and control of your devices and buildings
Please note the words within *(stars) must be accentuated in some way, please use your creative freedom.
A design that fits the look and feel of our brand, as seen in our website here: https://brindlewavesys.example/ is encouraged

```html
<!DOCTYPE html>
<html lang="en">
<head>
<meta charset="utf-8">
<title>Brindlewave Systems – Retractable Banner</title>
<link rel="stylesheet" href="https://fonts.googleapis.com/css2?family=Montserrat:wght@400;500;600;800&display=swap">
<style>
  :root {
    --stage: #8a8384;
    --white: #ffffff;
    --navy: #243447;
    --ink: #2b3a4a;
    --teal: #13a9ba;
    --teal-deep: #0e5f6c;
    --royal: #1f5fbf;
    --panel-top: #e6f2f9;
    --panel-bottom: #f3f8fc;
    --sky-top: #6fb4e6;
    --sky-low: #cfe6f5;
    --city: #9fb4bf;
    --water: #4f8e8f;
  }
  * { margin: 0; padding: 0; box-sizing: border-box; }
  html, body {
    width: 1200px; height: 2222px; overflow: hidden;
    background: var(--stage);
  }
  .banner {
    position: absolute; left: 212px; top: 98px;
    width: 777px; height: 2024px;
    background: var(--white);
    box-shadow: 4px 6px 14px rgba(0,0,0,.35);
    overflow: hidden;
    font-family: "Montserrat", Arial, sans-serif;
    color: var(--ink);
  }
  .banner-shapes { position: absolute; inset: 0; width: 777px; height: 2024px; }
  .brand { position: absolute; left: 150px; top: 72px; display: flex; align-items: center; gap: 22px; }
  .brand-mark { width: 92px; height: 92px; border-radius: 50%; background: var(--teal); }
  .brand-name { font-weight: 600; color: var(--navy); line-height: 1; }
  .brand-name .line-1 { display: block; font-size: 50px; letter-spacing: -0.5px; }
  .brand-name .line-2 { display: block; font-size: 20px; letter-spacing: 14px; margin-top: 8px; padding-left: 4px; }
  .copy { position: absolute; left: 0; width: 777px; text-align: center; color: var(--ink); }
  .copy strong { font-weight: 800; color: var(--navy); }
  .headline { top: 933px; font-size: 44px; line-height: 61px; font-weight: 500; }
  .statement { font-size: 46px; line-height: 69.5px; font-weight: 400; }
  .statement-iot { top: 1086px; }
  .statement-monitoring { top: 1315px; }
  .divider { position: absolute; left: 24px; width: 725px; border-top: 2px dashed #4a5560; }
  .divider-1 { top: 1066px; }
  .divider-2 { top: 1304px; }
  .web-icon { position: absolute; left: 362px; top: 1756px; width: 54px; height: 54px; }
  .web-address { position: absolute; left: 0; top: 1820px; width: 777px; text-align: center;
    font-size: 40px; font-weight: 600; color: var(--white); letter-spacing: .3px; }
  .phone-pill { position: absolute; left: 34px; top: 1886px; width: 708px; height: 98px;
    background: var(--white); border-radius: 49px;
    display: flex; align-items: center; justify-content: center; gap: 16px; }
  .phone-icon { width: 58px; height: 58px; }
  .phone-number { font-size: 58px; font-weight: 800; color: var(--navy); letter-spacing: -1px; }
</style>
</head>
<body>
<div class="banner">
  <svg class="banner-shapes" viewBox="0 0 699 1822" preserveAspectRatio="none" aria-hidden="true">
    <defs>
      <linearGradient id="scene-tones" x1="0" y1="0" x2="0" y2="1">
        <stop offset="0" stop-color="var(--sky-top)"/>
        <stop offset="0.45" stop-color="var(--sky-low)"/>
        <stop offset="0.7" stop-color="var(--city)"/>
        <stop offset="1" stop-color="var(--water)"/>
      </linearGradient>
      <linearGradient id="panel-tones" x1="0" y1="0" x2="0" y2="1">
        <stop offset="0" stop-color="var(--panel-top)"/>
        <stop offset="1" stop-color="var(--panel-bottom)"/>
      </linearGradient>
    </defs>
    <!-- city scene area -->
    <path d="M0 190 Q340 330 699 195 L699 800 L0 800 Z" fill="url(#scene-tones)"/>
    <!-- top blue sweep -->
    <path d="M0 155 Q340 300 699 178 L699 196 Q340 330 0 196 Z" fill="var(--royal)"/>
    <!-- teal sweep under scene -->
    <path d="M0 640 Q140 760 360 772 Q560 775 699 712 L699 1822 L0 1822 Z" fill="var(--teal)"/>
    <path d="M0 690 Q130 795 350 803 Q560 805 699 722 L699 1822 L0 1822 Z" fill="var(--teal-deep)"/>
    <!-- content panel -->
    <path d="M0 735 Q140 830 350 835 Q560 835 699 745 L699 1822 L0 1822 Z" fill="url(#panel-tones)"/>
    <!-- footer sweep -->
    <path d="M0 1455 Q330 1560 699 1382 L699 1822 L0 1822 Z" fill="var(--teal-deep)"/>
    <path d="M0 1462 Q340 1592 699 1420 L699 1822 L0 1822 Z" fill="var(--white)"/>
    <path d="M0 1475 Q340 1605 699 1445 L699 1822 L0 1822 Z" fill="var(--teal)"/>
  </svg>
  <div role="img" aria-label="Photograph of a waterfront city skyline with a tall tower under a blue sky" style="position:absolute;left:0;top:250px;width:777px;height:520px;"></div>

  <div class="brand">
    <div class="brand-mark"></div>
    <div class="brand-name"><span class="line-1">Brindlewave</span><span class="line-2">SYSTEMS</span></div>
  </div>

  <p class="copy headline">Your <strong>Data Collection</strong><br><strong>Problems</strong> End Here</p>
  <div class="divider divider-1"></div>
  <p class="copy statement statement-iot">Our technology transforms<br>any building into an <strong>IoT</strong><br><strong>Smart Building</strong></p>
  <div class="divider divider-2"></div>
  <p class="copy statement statement-monitoring">Our <strong>Monitoring &amp; Alerting</strong><br>capabilities give you full<br>insight &amp; control of your<br>devices and buildings</p>

  <svg class="web-icon" viewBox="0 0 54 54" aria-hidden="true" fill="none" stroke="var(--white)" stroke-width="2.5">
    <circle cx="27" cy="27" r="25"/>
    <circle cx="27" cy="27" r="15"/>
    <ellipse cx="27" cy="27" rx="6.5" ry="15"/>
    <line x1="12" y1="27" x2="42" y2="27"/>
    <line x1="15" y1="20" x2="39" y2="20"/>
    <line x1="15" y1="34" x2="39" y2="34"/>
  </svg>
  <p class="web-address">www.brindlewavesys.example</p>

  <div class="phone-pill">
    <svg class="phone-icon" viewBox="0 0 58 58" aria-hidden="true" fill="none" stroke="var(--navy)" stroke-width="3" stroke-linejoin="round">
      <path d="M14 8 L22 8 L26 19 L20 24 Q26 35 34 38 L39 32 L50 36 L50 44 Q48 50 40 50 Q20 46 10 20 Q10 10 14 8 Z"/>
      <path d="M33 10 Q45 12 48 24"/>
      <path d="M32 17 Q39 18 41 25"/>
    </svg>
    <span class="phone-number">+1 (800) 555-0142</span>
  </div>
</div>
</body>
</html>
```